Business Card Design using new attached logo

We are a family run Plumbing and Heating firm looking to improve our company image with an improved business card and new logo.We are looking to keep the company colour (Blue) involved in our design

Reason: New logo added which needs to be incorporated on designs

Industry/Entity Type

Business

Contact Information for Business Card

See attachment of all info required.

Requirements
Must have
• We have just picked a new company logo which is attached.
• Could you please provide your business card designs using this logo.
• We are looking for the logo on the back as well as the front with all the info required

```html
<!DOCTYPE html>
<html lang="en">
<head>
<meta charset="utf-8">
<title>Calder Flow Ltd. – Business Cards</title>
<link rel="stylesheet" href="https://fonts.googleapis.com/css2?family=Didact+Gothic&family=Montserrat:wght@700&display=swap">
<style>
  :root {
    --page-bg: #ecebe9;
    --card-white: #ffffff;
    --brand-blue: #1b7cc4;
    --brand-navy: #26408a;
    --ink: #1d1d1f;
    --ink-soft: #3a3a3c;
    --shadow: rgba(0, 0, 0, 0.12);
  }
  * { box-sizing: border-box; margin: 0; padding: 0; }
  html, body {
    width: 1200px;
    height: 856px;
    overflow: hidden;
    background: var(--page-bg);
  }
  .sheet {
    position: relative;
    width: 1200px;
    height: 856px;
  }
  .card {
    position: absolute;
    top: 270px;
    width: 520px;
    height: 316px;
    border-radius: 30px;
    overflow: hidden;
    box-shadow: 0 10px 28px var(--shadow);
  }

  /* Front */
  .card--front {
    left: 60px;
    background: var(--card-white);
    font-family: "Didact Gothic", sans-serif;
    color: var(--ink);
  }
  .brand-dot {
    position: absolute;
    left: 40px;
    top: 92px;
    width: 118px;
    height: 118px;
    border-radius: 50%;
    background: linear-gradient(135deg, var(--brand-blue), var(--brand-navy));
  }
  .brand-name {
    position: absolute;
    left: 172px;
    top: 118px;
    font-family: "Montserrat", sans-serif;
    font-weight: 700;
    font-size: 14px;
    letter-spacing: 0.02em;
    color: var(--brand-blue);
  }
  .person {
    position: absolute;
    left: 172px;
    top: 146px;
  }
  .person__name {
    font-family: "Montserrat", sans-serif;
    font-weight: 700;
    font-size: 16px;
    color: var(--ink);
  }
  .person__role {
    font-size: 13px;
    color: var(--ink-soft);
    margin-top: 2px;
  }
  .contact-list {
    position: absolute;
    left: 172px;
    top: 198px;
    list-style: none;
    font-size: 15px;
    line-height: 1.45;
    color: var(--ink);
  }
  .contact-list li,
  .back-details li {
    display: flex;
    align-items: center;
    gap: 6px;
  }
  .icon { flex: none; }

  /* Back */
  .card--back {
    left: 620px;
    background: linear-gradient(120deg, var(--brand-blue) 0%, var(--brand-navy) 100%);
    font-family: "Didact Gothic", sans-serif;
    color: var(--card-white);
  }
  .back-disc {
    position: absolute;
    left: -60px;
    top: -40px;
    width: 380px;
    height: 380px;
    border-radius: 50%;
    background: var(--card-white);
  }
  .back-brand {
    position: absolute;
    left: 30px;
    top: 144px;
    font-family: "Montserrat", sans-serif;
    font-weight: 700;
    font-size: 24px;
    letter-spacing: 0.02em;
    color: var(--brand-blue);
  }
  .back-details {
    position: absolute;
    left: 338px;
    top: 62px;
    list-style: none;
    font-size: 13px;
    line-height: 1.6;
  }
</style>
</head>
<body>
<main class="sheet">

  <section class="card card--front" aria-label="Business card front">
    <div class="brand-dot"></div>
    <div class="brand-name">CALDER FLOW LTD.</div>
    <div class="person">
      <div class="person__name">MARTIN HALE</div>
      <div class="person__role">Director</div>
    </div>
    <ul class="contact-list">
      <li>
        <svg class="icon" width="13" height="13" viewBox="0 0 16 16" aria-hidden="true">
          <circle cx="8" cy="8" r="8" fill="#1b7cc4"/>
          <path d="M5.4 4.2l1.3 1.6-.8 1c.5 1.1 1.3 1.9 2.3 2.4l1-.8 1.6 1.3-.6 1.4c-2.9-.4-5.3-2.8-5.7-5.7z" fill="#fff"/>
        </svg>
        07700 900412
      </li>
      <li>
        <svg class="icon" width="13" height="13" viewBox="0 0 16 16" aria-hidden="true">
          <circle cx="8" cy="8" r="8" fill="#1b7cc4"/>
          <rect x="4" y="5.2" width="8" height="5.6" rx="0.8" fill="#fff"/>
          <path d="M4.3 5.6L8 8.4l3.7-2.8" stroke="#1b7cc4" stroke-width="0.9" fill="none"/>
        </svg>
        martinhale@calderflow.co.uk
      </li>
    </ul>
  </section>

  <section class="card card--back" aria-label="Business card back">
    <div class="back-disc"></div>
    <div class="back-brand">CALDER FLOW</div>
    <ul class="back-details">
      <li>14 Mill Parade,</li>
      <li>Ash Road, Lenwood,</li>
      <li>Surrey LW4 2JT</li>
      <li>
        <svg class="icon" width="12" height="12" viewBox="0 0 16 16" aria-hidden="true">
          <circle cx="8" cy="8" r="8" fill="#fff"/>
          <path d="M5.4 4.2l1.3 1.6-.8 1c.5 1.1 1.3 1.9 2.3 2.4l1-.8 1.6 1.3-.6 1.4c-2.9-.4-5.3-2.8-5.7-5.7z" fill="#26408a"/>
        </svg>
        020 7946 0321
      </li>
      <li>
        <svg class="icon" width="12" height="12" viewBox="0 0 16 16" aria-hidden="true">
          <circle cx="8" cy="8" r="8" fill="#fff"/>
          <rect x="5.5" y="3.8" width="5" height="3" fill="#26408a"/>
          <rect x="4" y="6.6" width="8" height="4" rx="0.8" fill="#26408a"/>
          <rect x="5.5" y="9.4" width="5" height="2.6" fill="#fff" stroke="#26408a" stroke-width="0.8"/>
        </svg>
        020 7946 0587
      </li>
    </ul>
  </section>

</main>
</body>
</html>
```